Create a packaging design for a new deodorant

New product container label. The jar is 2.75" in diameter and 2.75" high. The (transparent) label size is 1.5" by 8.5" and will wrap nearly fully around the jar when applied. Approximately 3.25" of the label will be devoted to the name and front section of the jar (what I am requesting you to design). Remaining part of the label will include a brief description, directions, general warning, ingredients, manufacturer, distributor, and barcode. The deodorant name is ZEF. It is a clear colorless solution, ecologically friendly, naturally occurring deodorant salt solution. Water based, no alcohol, non-sticky, non-waxy, non-staining, just simple, clean and effective. Nature's way of getting the job done. Label to use transparent green and/or blue colors. Phrases such as " Fresh as a Springtime shower" or "Fresh as an ocean breeze" might be used. The deodorant has a NEW, unique, revolutionary applicator.

Target Market(s)

All adult men and women

Industry/Entity Type

Product

Number of Pages Required

1 page

Requirements
Nice to have
• ZEF
• This is a new deodorant, a simple but elegant solution to an age-old problem.
• Why I Hate Deodorants
• I’ve had my share of problems with deodorants, and with antiperspirants for that matter, too. First off, the last thing I want to do when I step out of the shower is to put some sticky, slimy, or waxy goop on clean skin. I don’t like it when it feels like skin sticks together in skin folds. When I used to use the old stick deodorants, I would periodically scrape the edge of the plastic container against my skin and cause an abrasion that would then be irritated for the next 3 days. This would be particularly true when I got down to the bottom of the stick and the medication surface flattened out in the dispenser. Sometimes the deodorant or antiperspirant itself would cause such abrasions to grow red and angry and force me to stop using it altogether for the next week. Then I’d be hunting (and hurting) for alternatives. So every few months I would spend lots of time in the store looking at all the different brands of deodorants to find something that was a bit different - less caustic, less sticky, less stinky, or in a different dispenser that might work better for me. Roll-on deodorants work for me until they don’t. Half the time I’m trying to hold the bottle upside down and squeezing it so the product comes out. The other half of the time the roller ball gets stuck and I’m trying to get it to turn. What a waste of time. Or if it pours out, I have to spread it all over the place to get it thin enough to dry out. I dispensed with antiperspirants years ago when I had to throw away some of my favorite shirts because of sweat (really antiperspirant chemical) stains. I’ve also seen enough people with hidradenitis (infected sweat glands from using some antiperspirants) to know that some of these products that clog skin pores can be serious skin irritants.
• I’m a Natural Kind of Guy
• Don’t get me wrong. I’m not a tree hugger. I haven’t been out on the high seas in a rowboat maneuvering between a harpooner and a whale. But by the same token I don’t buy 3-step hair treatments. I don’t color my hair either. I don’t lounge around in bubble baths. And I don’t like to use heavy-scented cleansers, shampoos or skin products. I’m just looking for something clean, plain and simple ...something that works, that’s safe and dependable. Maybe even a natural product that has a long track record of safety and effectiveness.
• Just try it.....(There’s nothing more we’ll need to say!!)
• ZEF uses a natural mineral salt, water, and a preservative. Nothing more. ZEF has a unique and patented dispenser. The dispenser was made for the product and made for the job. One swipe application and you’re done! YOU can control the amount of deodorant applied by the sponge applicator. ZEF is WATER-BASED. NO ALCOHOL. NO CHEMICALS. NO IRRITANTS. It dries quickly. No drips like you can get from spray bottles. The applicator doesn’t clog up or stop rolling. And it NEVER stains clothing. It’s just simple...easy...effective. And with a simple product we don’t have to charge a lot of money for it. So it’s inexpensive, too. I know you’re going to like this product.
• Swipe it on.... Odor gone!

```html
<!DOCTYPE html>
<html lang="en">
<head>
<meta charset="utf-8">
<title>ZEF Deodorant – Front Label</title>
<link href="https://fonts.googleapis.com/css2?family=Cabin:wght@400;700&display=swap" rel="stylesheet">
<style>
  :root {
    --page-bg: #efefef;
    --label-dark: #2d2d2d;
    --brand-red: #b3151b;
    --badge-blue: #1d8fd1;
    --tag-green: #8dc43d;
    --ink-white: #ffffff;
  }
  * { margin: 0; padding: 0; box-sizing: border-box; }
  html, body {
    width: 1200px;
    height: 849px;
    overflow: hidden;
    background: var(--page-bg);
    font-family: "Cabin", "Gill Sans", sans-serif;
  }
  .canvas {
    position: relative;
    width: 1200px;
    height: 849px;
  }
  .front-label {
    position: absolute;
    left: 228px;
    top: 170px;
    width: 745px;
    height: 510px;
  }
  .label-shape {
    position: absolute;
    inset: 0;
    width: 745px;
    height: 510px;
  }
  .label-shape polygon { fill: var(--label-dark); }
  .name-block {
    position: absolute;
    left: 168px;
    top: 39px;
    width: 448px;
    height: 258px;
    background: var(--brand-red);
  }
  .brand-name {
    position: absolute;
    left: 22px;
    top: 8px;
    font-weight: 700;
    font-size: 190px;
    line-height: 1;
    letter-spacing: 2px;
    color: var(--ink-white);
  }
  .product-type {
    position: absolute;
    right: 6px;
    bottom: 6px;
    font-weight: 400;
    font-size: 30px;
    line-height: 1;
    color: var(--ink-white);
  }
  .new-badge {
    position: absolute;
    left: 101px;
    top: 6px;
    width: 112px;
    height: 66px;
    background: var(--badge-blue);
    border: 4px solid var(--ink-white);
    color: var(--ink-white);
    font-weight: 700;
    font-size: 42px;
    line-height: 58px;
    text-align: center;
  }
  .tagline {
    position: absolute;
    left: 420px;
    top: 297px;
    width: 218px;
    height: 96px;
    background: var(--tag-green);
    color: var(--ink-white);
    font-size: 29px;
    line-height: 40px;
    padding: 7px 8px;
    white-space: nowrap;
  }
  .claims {
    position: absolute;
    left: 188px;
    top: 312px;
    list-style: none;
    color: var(--ink-white);
    font-size: 32px;
    line-height: 48px;
    white-space: nowrap;
  }
</style>
</head>
<body>
  <main class="canvas">
    <section class="front-label">
      <svg class="label-shape" viewBox="0 0 745 510" aria-hidden="true">
        <polygon points="62,6 670,22 745,235 700,448 196,510 84,398 6,140"/>
      </svg>
      <div class="name-block">
        <span class="brand-name">ZEF</span>
        <span class="product-type">DEODORANT</span>
      </div>
      <div class="new-badge">NEW</div>
      <ul class="claims">
        <li>WATER-BASED</li>
        <li>NO ALCOHOL</li>
        <li>NO CHEMICALS</li>
        <li>NO IRRITANTS</li>
      </ul>
      <p class="tagline">SWIPE IT ON....<br>ODOR GONE!</p>
    </section>
  </main>
</body>
</html>
```